Striking new Advert required for Commercial Real Estate Agency

We need a a NEW newspaper advertisement for the marketing of a large commercial property (a Backpackers lodge)

Dimensions are to be width of 101mm and height of 100mm (10cms)

Our key design statement for this advert is clean, modern and minimalist design, with accents of 'HOT PINK' colour to remove it from looking too boring, perhaps in the area of the contact icons. The heirachy of the advert is outlined in the attached ADVERTISEMENT TEXT FILE.

Our company name is THE MERIDAL COLLECTIVE, and we want our brand to appear professional yet classy in it's design style (sort of like an advertising or design agency)

We have two logo options below, one more square in its layout (which we prefer) and the other more rectangular, which may be better suited for the layout. We are not adverse to the logo being reversed (white text on black), along with other key element areas such as the main advert heading and the "FOR SALE" part, and think this would be a good option.
There are two photos attached to be included in the advert.

We have attached an example of an old advert that we did, which we DID NOT LIKE, and which was for a smaller width than the one we need (it is only 65% of the width of this one). WE have also atached a file showing layout of some of our competitors adverts, which we dont think are too good either.

We are really open for ideas, but have time pressures, so please come back with any questions as soon as you can, if needed.

Thank you
Updates

Thank you for the great and diverse designs. There are a few standout options, but one style that we prefer most.

Target Market(s)

We are wanting this newspaper advertisement to attract interest from real estat e developers, investors and motel/lodge owners, along with other high nett worth individuals

Industry/Entity Type

Real Estate

Font styles to use
Serif
Sans Serif

Colors
1b1b1b
a54499
474747
fbfbfb

Requirements
Must have
• Clean modern look, predominantly monochromatic or black and white, with the hot pink accent somewhere, as mentioned above.
• All the contents of the TEXT provided, perhaps with additional space to add a little more if needed, Please advise if you think we dont have enough space for all of the TEXT
Should not have
• Script like fonts
• Cartoonish characters
• a 'cheap' look

```html
<!DOCTYPE html>
<html lang="en">
<head>
<meta charset="utf-8">
<title>For Sale – Mount Halloway Land Grab</title>
<link rel="stylesheet" href="https://fonts.googleapis.com/css2?family=Montserrat:wght@400;500;800&family=Source+Sans+3:wght@400;600;700&display=swap">
<style>
  :root {
    --ink: #1b1b1b;
    --accent: #a54499;
    --band: #474747;
    --paper: #fbfbfb;
    --backdrop: #d9d9d9;
    --body-text: #2a2a2a;
  }
  * { box-sizing: border-box; margin: 0; padding: 0; }
  html, body { width: 1200px; height: 903px; overflow: hidden; }
  body {
    background: var(--backdrop);
    font-family: "Source Sans 3", "Myriad Pro", sans-serif;
    color: var(--body-text);
    position: relative;
  }
  .advert {
    position: absolute;
    left: 160px; top: 16px;
    width: 880px; height: 870px;
    background: var(--paper);
    display: flex; flex-direction: column;
  }
  .advert-header {
    height: 96px;
    display: flex; align-items: flex-end; justify-content: space-between;
    padding: 0 44px 8px 40px;
  }
  .headline {
    font-family: "Montserrat", sans-serif;
    font-weight: 800; font-size: 72px; line-height: 1;
    color: var(--ink); letter-spacing: 0.5px;
  }
  .tagline {
    font-size: 27px; font-weight: 400; color: var(--ink);
    padding-bottom: 4px;
  }
  .property-photo {
    height: 249px;
    background: linear-gradient(180deg, #7fa9d6 0%, #b9cfe4 30%, #e6e6e2 55%, #9fa48a 80%, #4f6b34 100%);
  }
  .address-band {
    height: 64px; background: var(--band);
    display: flex; align-items: center; justify-content: center;
    font-family: "Montserrat", sans-serif; font-weight: 400;
    font-size: 28px; color: #fff; letter-spacing: 0.3px;
  }
  .details {
    flex: 1;
    padding: 6px 46px 0 40px;
    font-size: 23px; line-height: 1.3;
  }
  .intro { color: var(--body-text); }
  .lead {
    color: var(--accent); font-weight: 700;
    margin-top: 6px; line-height: 1.28;
  }
  .features { list-style: none; margin-top: 4px; }
  .features li {
    position: relative; padding-left: 34px;
    text-align: justify; margin-bottom: 7px;
  }
  .features li::before {
    content: ""; position: absolute; left: 9px; top: 12px;
    width: 9px; height: 9px; border-radius: 50%; background: var(--accent);
  }
  .features sup { font-size: 13px; }
  .tender {
    text-align: center; color: var(--accent);
    font-weight: 700; margin-top: 6px;
  }
  .contact-bar {
    height: 122px; background: var(--ink); color: #fff;
    display: flex; align-items: center;
    padding: 0 46px 0 40px;
  }
  .agent { width: 216px; }
  .agent-name { font-size: 25px; font-weight: 600; margin-bottom: 4px; }
  .contact-line {
    display: flex; align-items: center; gap: 12px;
    font-size: 23px; line-height: 1.35;
  }
  .contact-line svg { width: 17px; height: 17px; flex: none; }
  .agent-links { padding-top: 22px; width: 350px; }
  .brand {
    margin-left: auto;
    display: flex; align-items: center; gap: 14px;
  }
  .brand-square {
    width: 58px; height: 58px; border: 3px solid #fff;
  }
  .brand-name {
    font-family: "Montserrat", sans-serif; font-weight: 500;
    font-size: 17px; line-height: 1.15; letter-spacing: 1px;
    text-transform: uppercase;
  }
</style>
</head>
<body>
  <article class="advert">
    <header class="advert-header">
      <h1 class="headline">FOR SALE</h1>
      <p class="tagline">Mount Halloway Land Grab</p>
    </header>

    <div class="property-photo" role="img" aria-label="Photograph of the white weatherboard two-storey lodge with bay windows, balconies and garden, under a blue sky"></div>

    <div class="address-band">Harbourlight Lodge, 42 Kestrel Street, Mount Halloway</div>

    <section class="details">
      <p class="intro">This Old Beauty has served many, and is now ripe for development.</p>
      <p class="lead">One of Mt Hal’s largest land areas, now offered with vacant possession, with key details being:</p>
      <ul class="features">
        <li>Large Land area of 2076m<sup>2</sup> with elevated sunny position and great outlook + access from Tarrant Street</li>
        <li>Existing Backpackers Lodge of 970m<sup>2</sup> providing multiple rooms with amenity areas</li>
        <li>Four adjacent sites also available, taking total land area to 4452m<sup>2</sup>, an unprecedented Land Offering in this popular cuity fringe location</li>
      </ul>
      <p class="tender">Now Selling by Closed Tender</p>
    </section>

    <footer class="contact-bar">
      <div class="agent">
        <p class="agent-name">Dane Whitcombe</p>
        <p class="contact-line">
          <svg viewBox="0 0 24 24" aria-hidden="true"><path fill="var(--accent)" d="M6.6 10.8c1.4 2.8 3.8 5.1 6.6 6.6l2.2-2.2c.3-.3.7-.4 1-.2 1.1.4 2.3.6 3.6.6.6 0 1 .4 1 1V20c0 .6-.4 1-1 1C10.6 21 3 13.4 3 4c0-.6.4-1 1-1h3.5c.6 0 1 .4 1 1 0 1.3.2 2.5.6 3.6.1.3 0 .7-.2 1z"/></svg>
          (04) 555 0182
        </p>
        <p class="contact-line">
          <svg viewBox="0 0 24 24" aria-hidden="true"><rect x="6" y="2" width="12" height="20" rx="2" fill="none" stroke="var(--accent)" stroke-width="2.4"/><circle cx="12" cy="18" r="1.3" fill="var(--accent)"/></svg>
          (021) 555 417
        </p>
      </div>
      <div class="agent-links">
        <p class="contact-line">
          <svg viewBox="0 0 24 24" aria-hidden="true"><rect x="3" y="6" width="18" height="12" fill="var(--accent)"/><path d="M3 6l9 7 9-7" fill="none" stroke="var(--ink)" stroke-width="1.6"/></svg>
          dane@meridalcollective.co.nz
        </p>
        <p class="contact-line">
          <svg viewBox="0 0 24 24" aria-hidden="true"><g fill="none" stroke="var(--accent)" stroke-width="1.8"><circle cx="12" cy="12" r="9"/><ellipse cx="12" cy="12" rx="4" ry="9"/><path d="M3 12h18M5 7.5h14M5 16.5h14"/></g></svg>
          www.meridalcollective.co.nz
        </p>
      </div>
      <div class="brand">
        <span class="brand-square" aria-hidden="true"></span>
        <p class="brand-name">The<br>Meridal<br>Collective</p>
      </div>
    </footer>
  </article>
</body>
</html>
```